Truck Drivers Using App w/Jobsite Checklist

Looking for an 8" x 11" flyer that conveys to our customers (roofing contractors) that our drivers have tablets in each truck that have an app with a jobsite checklist that gives contractors less real time notifications and mistakes are caught with photos.
Should read something like this:
Ever wonder if your material has been delivered? We've got a solution for that!
All Trucks are equipped with dash-mounted tablet.
Here's what you get access to:
- Real Time Email Confirmation of Delivery
- Photos of Material Placement
- Before/After Photo of Driveway
- Material List of Products Delivered
- Homeowner Sign Off
Maybe a collage of the different photos available.
Target Market(s)
Roofing/Building Contractors
Industry/Entity Type
Roofing
Requirements
Must have
- website: www.harborfinchdepot.com
- tagline: Building Relationships, Building Trust - a Tradition Since 1905
- Photoshop format for further editing
Nice to have
- A smooth look to it.
- A collage of the photos avail on app

```html
<!DOCTYPE html>
<html lang="en">
<head>
<meta charset="utf-8">
<title>Harbor Finch Depot – Delivery Confirmation Flyer</title>
<link href="https://fonts.googleapis.com/css2?family=Lato:ital,wght@0,400;0,700;0,900;1,700&display=swap" rel="stylesheet">
<style>
  :root{
    --paper:#d7d8da;
    --footer:#c6c7c9;
    --brand-blue:#1f56b8;
    --deep-blue:#173f8c;
    --navy:#1d2f6b;
    --ink:#1b1f2a;
    --white:#ffffff;
    --tick-ring:#e9c629;
    --tick-fill:#2b2f3a;
  }
  *{margin:0;padding:0;box-sizing:border-box}
  html,body{width:928px;height:1200px;overflow:hidden;background:var(--paper)}
  body{font-family:'Lato',sans-serif;color:var(--white)}
  .flyer{position:relative;width:928px;height:1200px;overflow:hidden;background:var(--paper)}
  .backdrop{position:absolute;inset:0;width:928px;height:1200px}
  .brand{position:absolute;left:72px;top:26px;width:240px;color:var(--ink)}
  .brand-mark{display:flex;align-items:center;gap:8px;margin-left:12px;height:56px}
  .brand-dot{width:24px;height:24px;border-radius:50%;background:var(--navy);flex:none}
  .brand-name{font-weight:900;font-size:15px;color:var(--navy);letter-spacing:.4px;white-space:nowrap}
  .tagline{position:absolute;top:70px;left:0;font-size:8.6px;font-weight:700;color:var(--ink);white-space:nowrap}
  .website{position:absolute;top:93px;left:12px;display:flex;align-items:center;gap:8px;font-size:10px;color:var(--white);white-space:nowrap}
  .website-icon{width:11px;height:11px;border-radius:50%;background:var(--white);opacity:.9}
  .headline{position:absolute;left:648px;top:130px;width:220px;text-align:center;
    font-style:italic;font-weight:700;font-size:21px;line-height:36px}
  .subline{position:absolute;left:615px;top:288px;width:246px;text-align:center;font-size:13px;line-height:16px}
  .access-title{position:absolute;left:100px;top:494px;width:220px;text-align:center;
    font-style:italic;font-weight:700;font-size:20px;line-height:36px}
  .features{position:absolute;left:442px;top:379px;list-style:none}
  .feature{display:flex;align-items:center;height:74.5px;font-size:18px}
  .feature svg{width:48px;height:48px;margin-right:18px;flex:none}
  .photo{position:absolute}
</style>
</head>
<body>
<div class="flyer">
  <svg class="backdrop" viewBox="0 0 773 1000" preserveAspectRatio="none" aria-hidden="true">
    <defs>
      <linearGradient id="houseTone" x1="0" y1="0" x2="1" y2="1">
        <stop offset="0" stop-color="#3b4660"/><stop offset=".6" stop-color="#4a5670"/><stop offset="1" stop-color="#6c7890"/>
      </linearGradient>
      <linearGradient id="yardTone" x1="0" y1="0" x2="1" y2="1">
        <stop offset="0" stop-color="#2a56a8"/><stop offset="1" stop-color="#123777"/>
      </linearGradient>
      <linearGradient id="dashTone" x1="0" y1="0" x2="0" y2="1">
        <stop offset="0" stop-color="#dfe3e8"/><stop offset=".22" stop-color="#c3c9cf"/>
        <stop offset=".4" stop-color="#8f969d"/><stop offset=".55" stop-color="#4a4e54"/>
        <stop offset="1" stop-color="#1f2226"/>
      </linearGradient>
    </defs>
    <rect x="0" y="293" width="773" height="677" fill="url(#yardTone)"/>
    <polygon points="235,293 773,293 773,648 365,648" fill="url(#houseTone)"/>
    <polygon points="0,320 250,195 235,293 365,648 0,648" fill="#2058bd"/>
    <polygon points="0,648 365,648 560,970 0,970" fill="#1a4aa6" opacity=".55"/>
    <polygon points="150,0 590,0 505,293 235,293" fill="url(#dashTone)"/>
    <polygon points="590,0 773,0 773,293 505,293" fill="var(--brand-blue)"/>
    <line x1="235" y1="293" x2="773" y2="293" stroke="#fff" stroke-width="1.5"/>
    <rect x="0" y="970" width="773" height="30" fill="var(--footer)"/>
  </svg>

  <div class="photo" role="img" aria-label="Truck cab dashboard on a highway with a dash-mounted tablet, driver pointing at the screen" style="left:180px;top:0;width:520px;height:352px"></div>
  <div class="photo" role="img" aria-label="Tiled residential roof under a blue sky" style="left:282px;top:352px;width:646px;height:426px"></div>

  <header class="brand">
    <div class="brand-mark"><span class="brand-dot"></span><span class="brand-name">HARBOR FINCH DEPOT</span></div>
    <p class="tagline">Building Relationships, Building Trust - a Tradition Since 1905</p>
    <p class="website"><span class="website-icon"></span>www.harborfinchdepot.com</p>
  </header>

  <h1 class="headline">Ever wonder if your material has been delivered?</h1>
  <p class="subline">We've got a solution for that! All Trucks are equipped with dash-mounted tablet.</p>

  <h2 class="access-title">Here's what you get<br>access to:</h2>
  <ul class="features">
    <li class="feature"><svg viewBox="0 0 48 48"><circle cx="24" cy="24" r="21" fill="var(--tick-fill)" stroke="var(--tick-ring)" stroke-width="2.5" stroke-dasharray="5 2"/><circle cx="24" cy="24" r="13" fill="#fff"/><path d="M18 24.5l4.2 4.2L30.5 19" fill="none" stroke="var(--tick-fill)" stroke-width="3.2" stroke-linecap="round" stroke-linejoin="round"/></svg>Real Time Email Confirmation of Delivery</li>
    <li class="feature"><svg viewBox="0 0 48 48"><circle cx="24" cy="24" r="21" fill="var(--tick-fill)" stroke="var(--tick-ring)" stroke-width="2.5" stroke-dasharray="5 2"/><circle cx="24" cy="24" r="13" fill="#fff"/><path d="M18 24.5l4.2 4.2L30.5 19" fill="none" stroke="var(--tick-fill)" stroke-width="3.2" stroke-linecap="round" stroke-linejoin="round"/></svg>Photos of Material Placement</li>
    <li class="feature"><svg viewBox="0 0 48 48"><circle cx="24" cy="24" r="21" fill="var(--tick-fill)" stroke="var(--tick-ring)" stroke-width="2.5" stroke-dasharray="5 2"/><circle cx="24" cy="24" r="13" fill="#fff"/><path d="M18 24.5l4.2 4.2L30.5 19" fill="none" stroke="var(--tick-fill)" stroke-width="3.2" stroke-linecap="round" stroke-linejoin="round"/></svg>Before/After Photo of Driveway</li>
    <li class="feature"><svg viewBox="0 0 48 48"><circle cx="24" cy="24" r="21" fill="var(--tick-fill)" stroke="var(--tick-ring)" stroke-width="2.5" stroke-dasharray="5 2"/><circle cx="24" cy="24" r="13" fill="#fff"/><path d="M18 24.5l4.2 4.2L30.5 19" fill="none" stroke="var(--tick-fill)" stroke-width="3.2" stroke-linecap="round" stroke-linejoin="round"/></svg>Material List of Products Delivered</li>
    <li class="feature"><svg viewBox="0 0 48 48"><circle cx="24" cy="24" r="21" fill="var(--tick-fill)" stroke="var(--tick-ring)" stroke-width="2.5" stroke-dasharray="5 2"/><circle cx="24" cy="24" r="13" fill="#fff"/><path d="M18 24.5l4.2 4.2L30.5 19" fill="none" stroke="var(--tick-fill)" stroke-width="3.2" stroke-linecap="round" stroke-linejoin="round"/></svg>Homeowner Sign Off</li>
  </ul>

  <div class="photo" role="img" aria-label="Flatbed truck loaded with wrapped roofing material" style="left:72px;top:797px;width:172px;height:172px;background:linear-gradient(180deg,#7fa9d6 0%,#9fb9d2 30%,#c9c2bd 48%,#d6cfca 62%,#3a3b3e 80%,#2a2b2e 100%)"></div>
  <div class="photo" role="img" aria-label="Delivery truck cab with boom crane" style="left:250px;top:797px;width:171px;height:172px;background:linear-gradient(180deg,#a9c7e4 0%,#dfe4ea 30%,#f2f3f5 55%,#7b7f86 78%,#26282c 100%)"></div>
  <div class="photo" role="img" aria-label="Driver in safety vest holding a tablet" style="left:427px;top:797px;width:171px;height:172px;background:linear-gradient(180deg,#eeeff1 0%,#e2e3e5 35%,#cdd75e 62%,#9aa6b6 82%,#5c6a86 100%)"></div>
  <div class="photo" role="img" aria-label="Concrete driveway before delivery" style="left:72px;top:974px;width:172px;height:172px;background:linear-gradient(150deg,#b9babc,#a7a8aa 55%,#8c8d8f)"></div>
  <div class="photo" role="img" aria-label="Bundles of roofing shingles placed on a roof" style="left:250px;top:974px;width:348px;height:172px;background:linear-gradient(180deg,#9fb6c8 0%,#e6e4de 30%,#d9d5cc 45%,#4a8fb5 62%,#3a76a0 78%,#2e3036 100%)"></div>
</div>
</body>
</html>
```